Label Design for RTD Cocktail Line Tovelin Spirits

Tovelin Spirits is a line of Indian-inspired artisan cocktails that "brings the bartender home" for professional men and women who like the finer things in life but don’t always have the time to treat themselves. No need for a multitude of expensive and hard-to-find ingredients, time consuming recipes, or a mixologist.

Our line of 3 open and serve cocktails blends a range of premium spirits with exotic ingredients so you can conveniently raise a glass for any of life’s celebrations.

Our bottle is the 750ml Claret bottle with Quarnet (screw cap) closure and will be covered entirely in a shrink sleeve (so potentially anything can be designed for any part of the bottle). We want the bottle to pop on the shelf so it should look different than what’s already out there (Velvet Moth, Galdrova, Merlusa ready to drink cocktails). We are looking for a sexy design that's polished/sleek.
Updates

Project Deadline Extended
Reason: Hello designers! Tovelin Spirits is so impressed with what we have received thus far and we would like to give some of the designers a few extra days to make the edits we requested. It's never too late to submit! Thank you all!

Industry/Entity Type

It Professional

Requirements
Must have
• Front of bottle
* “Tovelin Spirits” name and Peacock Logo- but feel free to pull the elements apart and use them on the bottle in different ways
* Open & Serve
* 12% ALC/VOL
* 750 ml
* 3 different labels in a theme for
-Borvelle
-Faluntera
-Pomadrine

Borvelle Ideas- soft brown palate, the ingredients in chai spice (cloves, cardamom pods, nutmeg, black peppercorns, star anise, and cinnamon stick)

Faluntera Ideas -cool and refreshing, pale green shade (not clashing with logo), graphics of fresh mint leaves, green chili, lime, cucumber

Pomadrine Ideas- soft/pale pink shades, graphics of lychi fruit (outer red shell and inner pink flesh), ginger

Back of bottle
* explanation of the 3 cocktails
Borvelle: Forget what you think you know about chai, this is not the Queen’s tea-time drink! Borvelle is a smooth, sweetly -spiced cocktail made with vodka, black tea, and a combination of aromatic spices. This velvety cocktail is rich without being heavy. Enjoy chilled or over ice anytime.

Faluntera: Faluntera can’t make up its mind! This fusion of zesty lime, sweet mint, earthy cucumber and spicy chilies is so refreshing you’ll crave it on a hot summer day or a cool winter’s night. The exotic botanicals in gin add a complexity to the cocktail making this a refreshing but potent drink! Enjoy chilled or over ice anytime.

Pomadrine: East meet West. Delicate lychi meet hard-hitting whiskey. Pomadrine will tempt you senses with flavor, fragrance and beauty. The peppery kick of ginger and the intensity of the un-aged whiskey are softened by lychi’s intoxicating scent and subtle, sweet finish.

Please include
1. Bottled By QRW Spirits Company
2. Sample barcode (where you would place it in your design)
3. www.TovelinSpirits.example
4. GOVERNMENT WARNING: (1) According to the Surgeon General, women should not drink alcoholic beverages during pregnancy because of the risk of birth defects. (2) Consumption of alcoholic beverages impairs your ability to drive a car or operate machinery, and may cause health problems.

Optional to include
*"Bring the Bartender Home"
*"Tovelin Spirits” name and Peacock Logo on the back
*Entirely black sleeve with contrasting design

FYI the Fonts used in our logo are Geosans Light and Prakrta, but feel free to use other complimentary fonts on the other aspects.
Nice to have
• Optional to include

```html
<!DOCTYPE html>
<html lang="en">
<head>
<meta charset="utf-8">
<title>Tovelin Spirits – Cocktail Sleeve Labels</title>
<link rel="stylesheet" href="https://fonts.googleapis.com/css2?family=Poiret+One&family=Didact+Gothic&display=swap">
<style>
  :root {
    --canvas: #ffffff;
    --mark-bg: #231f20;
    --mark-ink: #2a9fd6;
    --name-ink: #ffffff;

    --chai-top: #c4996b;
    --chai-strip: #8a5c3b;
    --chai-band: #7e3c1b;
    --chai-base: #c4996b;
    --chai-info: #5b4030;
    --chai-disc-a: #d9b27a;
    --chai-disc-b: #6b4024;

    --mint-top: #7aa23a;
    --mint-strip: #1c7a3e;
    --mint-band: #3a9442;
    --mint-strip-low: #117238;
    --mint-base: #0e5a38;
    --mint-info: #b9d7c0;
    --mint-disc-a: #b9df7a;
    --mint-disc-b: #2f8a3c;

    --lych-top: #ec068d;
    --lych-strip: #cf4760;
    --lych-band: #f6aebb;
    --lych-base: #f2809a;
    --lych-info: #6b3a46;
    --lych-disc-a: #ff8fc8;
    --lych-disc-b: #d81a78;
  }
  * { box-sizing: border-box; margin: 0; padding: 0; }
  html, body { width: 1200px; height: 900px; overflow: hidden; background: var(--canvas); }
  .canvas { position: relative; width: 1200px; height: 900px; }

  .sleeve { position: absolute; top: 0; width: 236px; height: 900px; overflow: hidden; background: var(--top); }
  .sleeve--chai { left: 148px; --top: var(--chai-top); --strip: var(--chai-strip); --band: var(--chai-band); --strip-low: var(--chai-strip); --base: var(--chai-base); --info: var(--chai-info); --disc-a: var(--chai-disc-a); --disc-b: var(--chai-disc-b); }
  .sleeve--mint { left: 471px; width: 234px; --top: var(--mint-top); --strip: var(--mint-strip); --band: var(--mint-band); --strip-low: var(--mint-strip-low); --base: var(--mint-base); --info: var(--mint-info); --disc-a: var(--mint-disc-a); --disc-b: var(--mint-disc-b); }
  .sleeve--lychee { left: 788px; --top: var(--lych-top); --strip: var(--lych-strip); --band: var(--lych-band); --strip-low: var(--lych-strip); --base: var(--lych-base); --info: var(--lych-info); --disc-a: var(--lych-disc-a); --disc-b: var(--lych-disc-b); }

  .band { position: absolute; left: 0; right: 0; top: 564px; height: 223px; background: var(--band); }
  .base { position: absolute; left: 0; right: 0; top: 787px; bottom: 0; background: var(--base); }
  .strip { position: absolute; left: 50%; width: 101px; margin-left: -50px; top: 473px; height: 91px; background: var(--strip); }
  .strip--low { top: 564px; height: 223px; background: var(--strip-low); }

  .brand-mark {
    position: absolute; left: 50%; top: 372px; width: 101px; height: 101px; margin-left: -50px;
    background: var(--mark-bg);
    display: flex; flex-direction: column; align-items: center; justify-content: flex-end;
    padding-bottom: 12px;
    font-family: "Didact Gothic", sans-serif; color: var(--mark-ink);
  }
  .brand-mark__name { font-size: 19px; line-height: 1; letter-spacing: 0.5px; }
  .brand-mark__sub { font-size: 7px; line-height: 1; letter-spacing: 3px; margin-top: 3px; text-transform: uppercase; }

  .flavour-name {
    position: absolute; left: 0; right: 0; top: 518px;
    text-align: center; font-family: "Poiret One", sans-serif;
    font-size: 44px; line-height: 1; color: var(--name-ink); white-space: nowrap;
  }

  .emblem {
    position: absolute; left: 50%; top: 638px; width: 92px; height: 92px; margin-left: -46px;
    border-radius: 50%;
    background: radial-gradient(circle at 45% 40%, var(--disc-a), var(--disc-b));
    box-shadow: 0 0 0 2px var(--strip-low), 0 0 0 3px var(--disc-a);
  }

  .serve-info {
    position: absolute; left: 0; right: 0; top: 832px;
    text-align: center; font-family: "Didact Gothic", sans-serif;
    font-size: 10px; line-height: 13px; color: var(--info);
  }
</style>
</head>
<body>
<main class="canvas">

  <section class="sleeve sleeve--chai">
    <div class="band"></div>
    <div class="base"></div>
    <div class="strip"></div>
    <div class="strip strip--low"></div>
    <div class="brand-mark"><span class="brand-mark__name">Tovelin</span><span class="brand-mark__sub">Spirits</span></div>
    <h2 class="flavour-name">Borvelle</h2>
    <div class="emblem" role="img" aria-label="Bronze spiral medallion evoking chai spices"></div>
    <p class="serve-info">Open &amp; Serve<br>12% ALC/VOL&nbsp; 750 ml</p>
  </section>

  <section class="sleeve sleeve--mint">
    <div class="band"></div>
    <div class="base"></div>
    <div class="strip"></div>
    <div class="strip strip--low"></div>
    <div class="brand-mark"><span class="brand-mark__name">Tovelin</span><span class="brand-mark__sub">Spirits</span></div>
    <h2 class="flavour-name">Faluntera</h2>
    <div class="emblem" role="img" aria-label="Green spiral medallion evoking mint, lime and chili"></div>
    <p class="serve-info">Open &amp; Serve<br>12% ALC/VOL&nbsp; 750 ml</p>
  </section>

  <section class="sleeve sleeve--lychee">
    <div class="band"></div>
    <div class="base"></div>
    <div class="strip"></div>
    <div class="strip strip--low"></div>
    <div class="brand-mark"><span class="brand-mark__name">Tovelin</span><span class="brand-mark__sub">Spirits</span></div>
    <h2 class="flavour-name">Pomadrine</h2>
    <div class="emblem" role="img" aria-label="Pink spiral medallion evoking lychee fruit"></div>
    <p class="serve-info">Open &amp; Serve<br>12% ALC/VOL&nbsp; 750 ml</p>
  </section>

</main>
</body>
</html>
```